In Home Senior Care Agency Business Card Design Needed

At Silver Birch Helpers, we don't just work in the care-giving industry. We truly care.

We are dedicated to providing personable, hands-on and integrated caring services that aim to help people maintain safe and comfortable life standards within the familiar settings of their own homes.

We would like to see designs that use my logo colors obviously. The final design will be modern, yet professional and semi-minimalistic. It should communicate an well-established company that is innovative. We would also like the design to have that 'flat' design look. Ideally having the design roll over to the backend of the card. Most likely it will be printed on a Matte paper with a die cut (either 2 rounded corners -leaf cut) or all rounded.

Target Market(s)

Baby boomer generation. 45 years and older.

Industry/Entity Type

Business

Contact Information for Business Card

Text for Front:
Slogan somewhere "Caring Hands. Familiar Homes.”

Darren Holloway
President

Cell: 512.608.7719
Phone: 512.274.6051
E: Darren@silverbirchhelpers.net
W: www.SilverBirchHelpers.net

Back:
-Meal Preparation
-Transportation
-Light Housekeeping
-Bathing Assistance
-Companionship

Font styles to use
Serif
Sans Serif

Requirements
Must have
• Flat, modern, professional design. Not too many colors. Match my colors in logo. Design of card must reflect from the front onto the back. Evenly spaced font.
Nice to have
• Try to work off current logo scheme, but logo may need to be redesigned.
Should not have
• Not too many colors.

```html
<!DOCTYPE html>
<html lang="en">
<head>
<meta charset="utf-8">
<title>Silver Birch Helpers — Business Card</title>
<link href="https://fonts.googleapis.com/css2?family=Cinzel:wght@400&family=Open+Sans:wght@400;700&display=swap" rel="stylesheet">
<style>
  :root {
    --page: #e9e6e1;
    --card: #1f2022;
    --card-edge: #2a2b2e;
    --silver: #a7a8aa;
    --grey-text: #b9babc;
    --gold: #f0a420;
    --logo-gold: #c9a640;
    --green: #2f8a22;
    --rule: #3a3b3e;
  }
  * { margin: 0; padding: 0; box-sizing: border-box; }
  html, body { width: 1200px; height: 900px; overflow: hidden; background: var(--page); }
  .canvas { position: relative; width: 1200px; height: 900px; }

  .card {
    position: absolute;
    width: 700px; height: 400px;
    background: linear-gradient(160deg, var(--card-edge), var(--card) 55%);
    border-radius: 6px;
    box-shadow: 0 10px 30px rgba(0,0,0,.18);
    color: var(--grey-text);
    font-family: "Open Sans", sans-serif;
  }
  .card--back { left: 90px; top: 40px; }
  .card--front { left: 410px; top: 460px; }

  /* Back side */
  .back-brand {
    position: absolute; left: 0; right: 0; top: 120px;
    display: flex; flex-direction: column; align-items: center; gap: 18px;
  }
  .brand-dot { width: 44px; height: 44px; border-radius: 50%; background: var(--silver); }
  .brand-name {
    font-family: "Cinzel", serif; font-weight: 400;
    font-size: 46px; color: var(--silver); letter-spacing: 1px;
  }
  .services {
    position: absolute; left: 0; right: 0; top: 272px;
    text-align: center; font-size: 13px; letter-spacing: 1.6px;
    text-transform: uppercase; line-height: 22px; color: var(--silver);
  }
  .services .sep { margin: 0 8px; }

  /* Front side */
  .front-brand {
    position: absolute; right: 44px; top: 44px;
    display: flex; align-items: center; gap: 12px;
  }
  .front-brand .brand-dot { width: 26px; height: 26px; background: var(--logo-gold); }
  .front-brand .brand-name { font-size: 27px; color: var(--logo-gold); letter-spacing: 0.5px; }

  .person { position: absolute; left: 60px; top: 148px; }
  .person-name { font-weight: 700; font-size: 24px; color: var(--gold); letter-spacing: 1px; text-transform: uppercase; }
  .person-title { font-size: 17px; color: var(--grey-text); margin-top: 2px; padding-left: 12px; }

  .contacts { position: absolute; top: 230px; font-size: 19px; line-height: 30px; }
  .contacts--phone { left: 72px; }
  .contacts--web { left: 370px; top: 140px; font-size: 16px; line-height: 26px; }
  .contact { display: flex; align-items: center; gap: 10px; }
  .contact svg { width: 16px; height: 16px; flex: none; }

  .rule { position: absolute; left: 40px; right: 40px; top: 318px; height: 1px; background: var(--rule); }
  .slogan {
    position: absolute; left: 0; right: 0; top: 330px; text-align: center;
    font-family: "Cinzel", serif; font-size: 20px; color: var(--green); letter-spacing: 1px;
  }
</style>
</head>
<body>
<main class="canvas">

  <section class="card card--back" aria-label="Card back">
    <div class="back-brand">
      <span class="brand-dot"></span>
      <span class="brand-name">Silver Birch Helpers</span>
    </div>
    <p class="services">
      Meal Preparation<span class="sep">|</span>Transportation<span class="sep">|</span>Light Housekeeping<br>
      Bathing Assistance<span class="sep">|</span>Companionship
    </p>
  </section>

  <section class="card card--front" aria-label="Card front">
    <div class="front-brand">
      <span class="brand-dot"></span>
      <span class="brand-name">Silver Birch Helpers</span>
    </div>

    <div class="person">
      <div class="person-name">Darren Holloway</div>
      <div class="person-title">President</div>
    </div>

    <div class="contacts contacts--phone">
      <div class="contact">
        <svg viewBox="0 0 16 16"><rect x="4" y="1" width="8" height="14" rx="1.5" fill="none" stroke="#f0a420" stroke-width="1.6"/><circle cx="8" cy="12.5" r="0.9" fill="#f0a420"/></svg>
        <span>512.608.7719</span>
      </div>
      <div class="contact">
        <svg viewBox="0 0 16 16"><path d="M1 6 Q8 1 15 6 L13 8 L11 6.5 L5 6.5 L3 8 Z" fill="#f0a420"/><rect x="3" y="9" width="10" height="5" rx="1" fill="#f0a420"/></svg>
        <span>512.274.6051</span>
      </div>
    </div>

    <div class="contacts contacts--web">
      <div class="contact">
        <svg viewBox="0 0 16 16"><rect x="1.5" y="3.5" width="13" height="9" rx="1" fill="#f0a420"/><path d="M1.5 4 L8 9 L14.5 4" fill="none" stroke="#1f2022" stroke-width="1.2"/></svg>
        <span>Darren@silverbirchhelpers.net</span>
      </div>
      <div class="contact">
        <svg viewBox="0 0 16 16"><rect x="2" y="6" width="7" height="4" rx="2" transform="rotate(-45 5.5 8)" fill="none" stroke="#f0a420" stroke-width="1.5"/><rect x="7" y="6" width="7" height="4" rx="2" transform="rotate(-45 10.5 8)" fill="none" stroke="#f0a420" stroke-width="1.5"/></svg>
        <span>www.SilverBirchHelpers.net</span>
      </div>
    </div>

    <div class="rule"></div>
    <p class="slogan">Caring Hands. Familiar Homes.</p>
  </section>

</main>
</body>
</html>
```